Test and Tag business card design

We are an appliance test and tag company in Brisbane Australia requiring a business card design.
I don't have a logo.
Card front: Matte black background with white font.
Card back: White background with black font colour
Examples are attached
Minimalist design
Reason: Looking for more designs with an extreme minimal feel
Industry/Entity Type
Appliance
Contact Information for Business Card
Business name: Harbor Check and Label
Description: Onsite Electrical Testing and Tagging
Licence No. 41853
Name: Greg Pellow
Mobile: 0418 526 937
Email: greg@harborcheckandlabel.com.au
Web: harborcheckandlabel.com.au
Logo Text
Harbor Check and Label
Look and feel

```html
<!DOCTYPE html>
<html lang="en">
<head>
<meta charset="utf-8">
<title>Harbor Check and Label – Business Card</title>
<link href="https://fonts.googleapis.com/css2?family=Cabin:wght@400;600;700&display=swap" rel="stylesheet">
<style>
  :root {
    --stage: #ededed;
    --card-dark-top: #3a3a3a;
    --card-dark-bottom: #242424;
    --card-light: #ffffff;
    --ink-light: #ffffff;
    --ink-dark: #222222;
    --shadow: rgba(0, 0, 0, 0.45);
  }
  html, body {
    margin: 0;
    padding: 0;
    width: 1200px;
    height: 1000px;
    overflow: hidden;
    background: var(--stage);
    font-family: "Cabin", Arial, sans-serif;
  }
  .canvas {
    position: relative;
    width: 1200px;
    height: 1000px;
  }
  .card {
    position: absolute;
    width: 688px;
    height: 397px;
    box-shadow: 5px 5px 6px var(--shadow);
  }
  .card--front {
    left: 48px;
    top: 77px;
    background: radial-gradient(ellipse at 50% 40%, var(--card-dark-top), var(--card-dark-bottom));
    color: var(--ink-light);
  }
  .card--back {
    left: 464px;
    top: 526px;
    background: var(--card-light);
    color: var(--ink-dark);
  }
  .wordmark {
    position: absolute;
    margin: 0;
    font-weight: 700;
    font-size: 30px;
    letter-spacing: -0.5px;
    white-space: nowrap;
    transform: translateX(-50%);
  }
  .card--front .wordmark { left: 197px; top: 178px; color: var(--ink-light); }
  .card--back .wordmark { left: 344px; top: 181px; color: var(--ink-dark); }
  .divider {
    position: absolute;
    left: 340px;
    top: 116px;
    width: 2px;
    height: 165px;
    background: var(--ink-light);
  }
  .contact {
    position: absolute;
    left: 368px;
    top: 126px;
  }
  .contact__name {
    margin: 0 0 14px;
    font-size: 33px;
    font-weight: 400;
    line-height: 1;
  }
  .contact__list {
    list-style: none;
    margin: 0;
    padding: 0;
    font-size: 17px;
  }
  .contact__item {
    display: flex;
    align-items: center;
    gap: 7px;
    height: 31px;
  }
  .contact__icon {
    width: 16px;
    height: 16px;
    flex: none;
  }
  .tagline {
    position: absolute;
    left: 0;
    right: 0;
    top: 336px;
    margin: 0;
    text-align: center;
    font-size: 17px;
    font-weight: 600;
  }
  .tagline__licence {
    font-size: 11px;
    font-weight: 600;
  }
  .web-address {
    position: absolute;
    left: 0;
    right: 0;
    top: 346px;
    margin: 0;
    text-align: center;
    font-size: 17px;
  }
</style>
</head>
<body>
<div class="canvas">

  <section class="card card--front" aria-label="Business card front">
    <p class="wordmark">Harbor Check &amp; Label</p>
    <div class="divider"></div>
    <div class="contact">
      <h1 class="contact__name">Greg Pellow</h1>
      <ul class="contact__list">
        <li class="contact__item">
          <svg class="contact__icon" viewBox="0 0 16 16" aria-hidden="true">
            <rect x="1" y="1" width="14" height="14" rx="2" fill="#fff"/>
            <path d="M5 4c-1 1-1 4 1 6s5 2 6 1l-1.5-1.5-1.3.8c-1-.5-2-1.5-2.5-2.5l.8-1.3z" fill="#2a2a2a"/>
          </svg>
          <span>0418 526 937</span>
        </li>
        <li class="contact__item">
          <svg class="contact__icon" viewBox="0 0 16 16" aria-hidden="true">
            <rect x="1" y="1" width="14" height="14" rx="2" fill="#fff"/>
            <rect x="3.5" y="5" width="9" height="6.5" fill="none" stroke="#2a2a2a" stroke-width="1.3"/>
            <path d="M3.5 5l4.5 3.5 4.5-3.5" fill="none" stroke="#2a2a2a" stroke-width="1.3"/>
          </svg>
          <span>greg@harborcheckandlabel.com.au</span>
        </li>
        <li class="contact__item">
          <svg class="contact__icon" viewBox="0 0 16 16" aria-hidden="true">
            <rect x="1" y="1" width="14" height="14" rx="2" fill="#fff"/>
            <circle cx="8" cy="8" r="4.5" fill="none" stroke="#2a2a2a" stroke-width="1.2"/>
            <path d="M3.5 8h9M8 3.5c-2 2.5-2 6.5 0 9M8 3.5c2 2.5 2 6.5 0 9" fill="none" stroke="#2a2a2a" stroke-width="1"/>
          </svg>
          <span>www.harborcheckandlabel.com.au</span>
        </li>
      </ul>
    </div>
    <p class="tagline">Onsite Electrical Testing &amp; Tagging – <span class="tagline__licence">Licence No. 41853</span></p>
  </section>

  <section class="card card--back" aria-label="Business card back">
    <p class="wordmark">Harbor Check &amp; Label</p>
    <p class="web-address">www.harborcheckandlabel.com.au</p>
  </section>

</div>
</body>
</html>
```